Create a business Card for a Women Owned Business Body Positive Company. The winner we hope to work with on other projects coming up for grand opening for flyers, postcards, email marketing, facebook page, stationary, labels, tshirt design....
We would like if possible in the background of the card a infinity symbol or crown if it fits into the design if not it's ok. But I am open to all suggestions we had alot problems with the our new logo being created this time sad to say :(

Our colors are Royal Purple, Grey, Black Thank you in advance for your talent, you hard work and your submissions!
Delia and Nadine :)
Updates

my Logo is velvet harbor boutique which is purple and has a heart and infinity sign in it and my colors are purple silver and black only of another card i had done nothing else. My logo is VELVET HARBOR BOUTIQUE LOGO

Industry/Entity Type

Retail

Contact Information for Business Card

website: www.velvtharborboutiques.example email: sales@velvetharborboutique.example
Delia Pruett & Nadine Kolb Owners

Font styles to use
Script

Colors
b768aa

Requirements
Must have
• COLORS ARE PURPLE BLACK AND GREY
Nice to have
• INFINITY SIGNING IN THE BACKGROUND

```html
<!DOCTYPE html>
<html lang="en">
<head>
<meta charset="utf-8">
<title>Velvet Harbor Boutique – Business Card</title>
<link rel="stylesheet" href="https://fonts.googleapis.com/css2?family=Dancing+Script:wght@500&family=Lato:wght@400&family=Quattrocento+Sans&display=swap">
<style>
  :root {
    --backdrop: #c9c9c9;
    --royal-purple: #5c2d85;
    --royal-purple-soft: #6a3a93;
    --brand-purple: #6b2f8f;
    --card-white: #f4f4f4;
    --card-white-edge: #e6e6e6;
    --ink: #4a4a4a;
    --ink-soft: #6d6d6d;
    --lilac-text: #eee4f4;
  }
  * { margin: 0; padding: 0; box-sizing: border-box; }
  html, body {
    width: 1200px;
    height: 576px;
    overflow: hidden;
    background: var(--backdrop);
  }
  .canvas {
    position: relative;
    width: 1200px;
    height: 576px;
  }
  .card {
    position: absolute;
    top: 138px;
    width: 484px;
    height: 294px;
    border-radius: 14px;
    overflow: hidden;
  }
  .card--front { left: 82px; }
  .card--back { left: 600px; }

  .card__pattern {
    position: absolute;
    inset: 0;
  }
  .card--front .card__pattern {
    background: linear-gradient(180deg, var(--royal-purple-soft), var(--royal-purple));
  }
  .card--back .card__pattern {
    background: linear-gradient(180deg, var(--card-white), var(--card-white-edge));
  }

  .brand-name {
    position: absolute;
    font-family: "Lato", sans-serif;
    font-weight: 400;
    text-transform: uppercase;
    letter-spacing: 0.04em;
    white-space: nowrap;
    transform: translateX(-50%);
    line-height: 1;
  }
  .card--front .brand-name {
    left: 242px;
    top: 156px;
    font-size: 20px;
    color: var(--lilac-text);
  }
  .card--back .brand-name {
    left: 340px;
    top: 92px;
    font-size: 16px;
    color: var(--brand-purple);
  }

  .owner-tab {
    position: absolute;
    left: -8px;
    top: 220px;
    width: 16px;
    height: 26px;
    border-radius: 0 13px 13px 0;
    background: var(--brand-purple);
  }
  .owners {
    position: absolute;
    left: 26px;
    top: 218px;
    white-space: nowrap;
    display: flex;
    align-items: baseline;
  }
  .owners__names {
    font-family: "Dancing Script", cursive;
    font-weight: 500;
    font-size: 22px;
    color: var(--brand-purple);
  }
  .owners__role {
    font-family: "Quattrocento Sans", sans-serif;
    font-size: 13px;
    color: var(--ink-soft);
    margin-left: 6px;
    padding-left: 6px;
    border-left: 1px solid var(--ink-soft);
    line-height: 16px;
  }
  .contact {
    position: absolute;
    left: 26px;
    top: 250px;
    font-family: "Quattrocento Sans", sans-serif;
    font-size: 12.5px;
    color: var(--ink);
    white-space: nowrap;
  }
  .contact__divider { margin: 0 4px; color: var(--ink-soft); }
  .contact__site-name { color: var(--brand-purple); }
</style>
</head>
<body>
<main class="canvas">
  <section class="card card--front" aria-label="Card front">
    <div class="card__pattern" role="img" aria-label="Faint repeating ornamental scroll pattern on royal purple"></div>
    <p class="brand-name">Velvet Harbor Boutique</p>
  </section>

  <section class="card card--back" aria-label="Card back">
    <div class="card__pattern" role="img" aria-label="Faint repeating ornamental scroll pattern on silver white"></div>
    <p class="brand-name">Velvet Harbor Boutique</p>
    <span class="owner-tab" aria-hidden="true"></span>
    <p class="owners">
      <span class="owners__names">Delia Pruett &amp; Nadine Kolb</span>
      <span class="owners__role">owners</span>
    </p>
    <p class="contact">
      <span class="contact__email">sales@velvetharborboutique.example</span><span class="contact__divider">|</span><span class="contact__site">www.<span class="contact__site-name">velvtharborboutiques</span>.example</span>
    </p>
  </section>
</main>
</body>
</html>
```